Awesome Office Furniture Dealer's Brochure!

Need a professional and informative brochure put together for our clients - may need separate designs for Government and Education clients. Should be based of our new website design and feel. Sections should include: Manufacturers we carry, services, and statements about our company - who we are & what we do. Brochure is 8.5 x 11 in tri-fold configuration. Template files attached.

Target Market(s)

Small to Medium businesses

Industry/Entity Type

Office Furniture

Requirements
Must have
• Look and feel of our website www.pembrills.com. Images can be taken from any of our vendors listed under /products, look to VEX primarily. We will get the final designer production ready images when needed.
Nice to have
• Incorporate the "love your workspace" from our website.

```html
<!DOCTYPE html>
<html lang="en">
<head>
<meta charset="utf-8">
<title>Pembrill's Office Furniture – Brochure Cover</title>
<link href="https://fonts.googleapis.com/css2?family=Montserrat:wght@500&family=Oswald:wght@400&family=Yellowtail&display=block" rel="stylesheet">
<style>
  :root {
    --backdrop: #b9b9b9;
    --paper: #f7f7f6;
    --brand-green: #6ab43e;
    --ink: #3a3a3c;
    --mist-grey: #a7a9ac;
    --ornament-tone: #dcdcdb;
    --photo-light: #dfe6e1;
    --photo-mid: #b9c7bf;
  }
  * { box-sizing: border-box; margin: 0; padding: 0; }
  html, body { width: 1200px; height: 800px; overflow: hidden; }
  body { background: var(--backdrop); position: relative; }

  .brochure-cover {
    position: absolute;
    left: 420px; top: 20px;
    width: 360px; height: 760px;
    background: var(--paper);
    overflow: hidden;
  }

  .brand {
    position: absolute;
    left: 40px; top: 36px;
    display: flex; align-items: center; gap: 12px;
  }
  .brand-dot {
    width: 34px; height: 34px; border-radius: 50%;
    background: var(--mist-grey);
    flex: none;
  }
  .brand-name {
    font-family: "Montserrat", sans-serif;
    font-weight: 500;
    color: var(--brand-green);
    line-height: 1;
  }
  .brand-name .primary { display: block; font-size: 30px; letter-spacing: 0.5px; }
  .brand-name .secondary { display: block; font-size: 10.5px; letter-spacing: 3.6px; margin-top: 5px; }

  .hero-art { position: absolute; left: 0; top: 0; width: 360px; height: 440px; }

  .tagline {
    position: absolute;
    left: 0; top: 456px; width: 100%;
    text-align: center;
    font-family: "Yellowtail", cursive;
    font-weight: 400;
    font-size: 46px;
    line-height: 46px;
    color: var(--brand-green);
  }

  .ornament-area {
    position: absolute;
    left: 60px; top: 572px;
    width: 240px; height: 40px;
    border-radius: 20px;
    background: var(--ornament-tone);
  }

  .contact {
    position: absolute;
    left: 0; top: 640px; width: 100%;
    text-align: center;
    font-family: "Oswald", sans-serif;
    color: var(--ink);
    text-transform: uppercase;
  }
  .contact .phone { font-size: 16px; letter-spacing: 0.2px; }
  .contact .phone .number { color: var(--brand-green); }
  .contact .web { font-size: 21px; margin-top: 2px; }

  .fold-edge { position: absolute; left: 0; bottom: 0; width: 100%; height: 6px; background: var(--brand-green); }
</style>
</head>
<body>
  <main class="brochure-cover">
    <svg class="hero-art" viewBox="0 0 360 440">
      <defs>
        <linearGradient id="officeTones" x1="0" y1="0" x2="1" y2="1">
          <stop offset="0" stop-color="#b9c7bf"/>
          <stop offset="0.55" stop-color="#dfe6e1"/>
          <stop offset="1" stop-color="#b9c7bf"/>
        </linearGradient>
      </defs>
      <path class="swoosh-top" d="M0,130 Q180,92 360,126 L360,140 Q180,110 0,142 Z" fill="#6ab43e"/>
      <path class="hero-photo" role="img" aria-label="Overhead view of an open-plan office with white desks, black task chairs and red lounge seating"
            d="M0,142 Q180,110 360,140 L360,352 Q180,425 0,336 Z" fill="url(#officeTones)"/>
      <path class="swoosh-bottom" d="M0,336 Q180,425 360,352 L360,362 Q180,440 0,348 Z" fill="#6ab43e"/>
      <path class="rule-line" d="M0,356 Q180,444 360,368" fill="none" stroke="#a7a9ac" stroke-width="2"/>
    </svg>

    <div class="brand">
      <span class="brand-dot"></span>
      <span class="brand-name">
        <span class="primary">PEMBRILL'S</span>
        <span class="secondary">OFFICE FURNITURE</span>
      </span>
    </div>

    <p class="tagline">Love your<br>workspace!</p>

    <div class="ornament-area" role="img" aria-label="Decorative arrow piercing a heart"></div>

    <div class="contact">
      <p class="phone">Call us: <span class="number">+ 555.014.2290</span></p>
      <p class="web">www.pembrills.com</p>
    </div>

    <div class="fold-edge"></div>
  </main>
</body>
</html>
```